Quiet Meadow Counseling business cards

Dana Korvath, LCPC, NCC
(555)347-0618
www.quietmeadowcounseling.example
dana@quietmeadowcounseling.example

Business cards. I would like it on the same background as pictured. Not on a white business card. I have attached the logo that was done by another designer with artbazaar. I am open to looking at single-sided and double-sided designs.

Target Market(s)

teenagers and adults

Industry/Entity Type

mental health

Contact Information for Business Card

Dana Korvath, LCPC, NCC (555)347-0618 dana@quietmeadowcounseling.example

Font styles to use
Other font styles liked:
• Cinzel

Colors

Designer to choose colors to be used in the design.

Requirements
Must have
• logo that is attached

```html
<!DOCTYPE html>
<html lang="en">
<head>
<meta charset="utf-8">
<title>Quiet Meadow Counseling – Business Cards</title>
<link href="https://fonts.googleapis.com/css2?family=Montserrat:wght@400;500;600&display=swap" rel="stylesheet">
<style>
  :root {
    --backdrop: #3a302b;
    --card-top: #2a4152;
    --card-bottom: #1b2c39;
    --name-blue: #2a93d8;
    --text-light: #e3e9ee;
    --accent-teal: #3fb3b0;
    --rule: rgba(225, 235, 242, 0.75);
    --divider: #2a7fb8;
    --mark: #d9e3ea;
  }
  * { box-sizing: border-box; margin: 0; padding: 0; }
  html, body {
    width: 1200px; height: 786px; overflow: hidden;
    background: var(--backdrop);
    font-family: "Montserrat", sans-serif;
  }
  .sheet {
    width: 1200px; height: 786px;
    display: flex; align-items: center; justify-content: center; gap: 40px;
  }
  .card {
    position: relative; width: 540px; height: 309px; overflow: hidden;
    border-radius: 4px;
    background: linear-gradient(160deg, var(--card-top), var(--card-bottom));
    box-shadow: 0 18px 40px rgba(0,0,0,0.45);
  }
  .card__decor {
    position: absolute; right: -60px; top: -40px; width: 320px; height: 320px;
    border-radius: 50%;
    background: radial-gradient(circle, rgba(120,170,180,0.16), rgba(120,170,180,0) 70%);
  }
  .brand { display: flex; flex-direction: column; align-items: center; }
  .brand__dot {
    width: 46px; height: 46px; border-radius: 50%;
    background: var(--accent-teal); margin-bottom: 12px;
  }
  .brand__name {
    color: var(--mark); font-weight: 600; text-transform: uppercase;
    text-align: center; letter-spacing: 1px; line-height: 1.35;
  }
  .brand__rule { display: block; height: 1px; background: var(--rule); margin: 4px auto 0; }

  /* contact side */
  .card--contact .brand { position: absolute; left: 28px; top: 92px; width: 190px; }
  .card--contact .brand__name { font-size: 15px; }
  .card--contact .brand__rule { width: 170px; }
  .contact {
    position: absolute; left: 238px; top: 98px;
    border-left: 1px solid var(--divider); padding-left: 16px;
  }
  .contact__name { color: var(--name-blue); font-size: 15px; font-weight: 600; margin-bottom: 10px; }
  .contact__line {
    display: flex; align-items: center; gap: 8px;
    color: var(--text-light); font-size: 11.5px; line-height: 20px;
  }
  .contact__line svg { width: 11px; height: 11px; flex: none; }

  /* logo side */
  .card--front .brand { position: absolute; left: 0; right: 0; top: 78px; }
  .card--front .brand__name { font-size: 21px; }
  .card--front .brand__rule { width: 300px; }
  .card--front .web {
    position: absolute; left: 0; right: 0; top: 232px; text-align: center;
    color: var(--accent-teal); font-size: 12px; letter-spacing: 0.3px;
  }
</style>
</head>
<body>
<main class="sheet">
  <section class="card card--contact">
    <div class="card__decor" role="img" aria-label="Faint leaf and swirl backdrop decoration"></div>
    <div class="brand">
      <span class="brand__dot"></span>
      <p class="brand__name">Quiet Meadow<br>Counseling</p>
      <span class="brand__rule"></span>
    </div>
    <div class="contact">
      <p class="contact__name">Dana Korvath, LCPC, NCC</p>
      <p class="contact__line">
        <svg viewBox="0 0 12 12"><path fill="#3fb3b0" d="M2.5 1l2 2.2-1 1.3a7 7 0 0 0 3 3l1.3-1 2.2 2-1.2 2C5 10.5 1.5 7 1 2.2z"/></svg>
        (555)347-0618
      </p>
      <p class="contact__line">
        <svg viewBox="0 0 12 12"><rect x="1" y="2.5" width="10" height="7" fill="#3fb3b0"/><path d="M1 2.5l5 4 5-4" fill="none" stroke="#1b2c39" stroke-width="1"/></svg>
        dana@quietmeadowcounseling.example
      </p>
      <p class="contact__line">
        <svg viewBox="0 0 12 12"><circle cx="6" cy="6" r="5" fill="#3fb3b0"/><path d="M1 6h10M6 1c-2.5 3-2.5 7 0 10M6 1c2.5 3 2.5 7 0 10" fill="none" stroke="#1b2c39" stroke-width="0.8"/></svg>
        www.quietmeadowcounseling.example
      </p>
    </div>
  </section>

  <section class="card card--front">
    <div class="card__decor" role="img" aria-label="Faint leaf and swirl backdrop decoration"></div>
    <div class="brand">
      <span class="brand__dot"></span>
      <p class="brand__name">Quiet Meadow<br>Counseling</p>
      <span class="brand__rule"></span>
    </div>
    <p class="web">www.quietmeadowcounseling.example</p>
  </section>
</main>
</body>
</html>
```